Houston Law Firm Business Card
Taven & Associates, PC 2013 Business Card
Professional
Dorian M. Taven
Trial Attorney
482 W. Birchfield Ave.
Suite 318
Houston, TX 77391
1-888-50-TAVEN
dorian.taven@tavenassociateslaw.example
tavenassociateslaw.example
Also include my blog:
lakeridgetrialcounsel.example

```html
<!DOCTYPE html>
<html lang="en">
<head>
<meta charset="utf-8">
<title>Taven &amp; Associates, PC — Business Card</title>
<link rel="stylesheet" href="https://fonts.googleapis.com/css2?family=Mulish:wght@400;600;700&display=swap">
<style>
  :root{
    --bg:#e4e3df;
    --card:#ffffff;
    --olive:#6b6a58;
    --olive-dark:#55544a;
    --grey:#8c8c8c;
    --grey-light:#d9d9d9;
    --ink:#4a4a4a;
    --ink-soft:#6f6f6f;
  }
  *{margin:0;padding:0;box-sizing:border-box}
  html,body{width:1200px;height:904px;overflow:hidden}
  body{background:var(--bg);font-family:"Mulish",Arial,sans-serif;color:var(--ink);position:relative}
  .card{position:absolute;left:260px;width:680px;height:389px;background:var(--card);
        box-shadow:0 6px 18px rgba(0,0,0,.18);overflow:hidden}
  .card--front{top:42px}
  .card--back{top:473px}

  /* front */
  .front-brand{position:absolute;left:0;right:0;top:145px;display:flex;justify-content:center;align-items:center;gap:16px}
  .brand-square{width:46px;height:46px;background:var(--olive);flex:none}
  .brand-name{font-weight:600;font-size:24px;letter-spacing:2px;text-transform:uppercase;color:var(--olive-dark);white-space:nowrap}
  .front-cities{position:absolute;left:0;right:0;top:262px;display:flex;justify-content:center;align-items:center;gap:12px;
        font-size:15px;letter-spacing:1px;color:var(--ink-soft)}
  .city-dot{width:7px;height:7px;border-radius:50%;background:var(--olive)}

  /* back */
  .back-band{position:absolute;left:0;top:0;width:250px;height:100%;
        background:linear-gradient(90deg,#c9c9c9 0%,#e6e6e6 45%,rgba(255,255,255,0) 100%)}
  .back-band-top{position:absolute;left:0;top:0;width:100%;height:140px;background:var(--card)}
  .back-brand{position:absolute;left:0;top:0;display:flex;align-items:center;gap:14px}
  .back-brand .brand-square{width:86px;height:96px}
  .back-brand .brand-name{font-size:17px;letter-spacing:1.5px}

  .person{position:absolute;left:100px;top:152px}
  .person-name{font-size:22px;font-weight:700;color:var(--olive-dark)}
  .person-title{font-size:13px;color:var(--ink-soft);margin-top:2px}

  .contact-left{position:absolute;left:100px;top:228px;font-size:14px;line-height:19px;color:var(--ink)}
  .contact-icons{position:absolute;left:68px;top:232px;display:flex;flex-direction:column;gap:5px}
  .contact-icons svg{width:14px;height:14px;fill:var(--grey)}
  .website{position:absolute;left:100px;top:318px;font-size:19px;letter-spacing:1px;color:var(--ink-soft)}
  .website-bar{position:absolute;left:0;top:352px;width:100%;height:2px;background:var(--grey-light)}

  .addresses{position:absolute;left:440px;top:30px;font-size:13px;line-height:18px;color:var(--ink)}
  .addresses p + p{margin-top:14px}
  .links{position:absolute;left:412px;top:232px;font-size:13px;line-height:22px;color:var(--ink)}
  .link-row{display:flex;align-items:center;gap:10px}
  .link-row svg{width:16px;height:16px;fill:var(--grey)}
</style>
</head>
<body>

<section class="card card--front" aria-label="Card front">
  <div class="front-brand">
    <span class="brand-square"></span>
    <span class="brand-name">Taven &amp; Associates, PC</span>
  </div>
  <div class="front-cities">
    <span>Houston</span><span class="city-dot"></span>
    <span>Cedar Hollow</span><span class="city-dot"></span>
    <span>Brookhaven</span>
  </div>
</section>

<section class="card card--back" aria-label="Card back">
  <div class="back-band"></div>
  <div class="back-band-top"></div>

  <div class="back-brand">
    <span class="brand-square"></span>
    <span class="brand-name">Taven &amp; Associates, PC</span>
  </div>

  <div class="person">
    <p class="person-name">Dorian M. Taven</p>
    <p class="person-title">Trial Attorney</p>
  </div>

  <div class="contact-icons">
    <svg viewBox="0 0 24 24"><path d="M6.6 10.8a15 15 0 0 0 6.6 6.6l2.2-2.2c.3-.3.7-.4 1-.2 1.1.4 2.3.6 3.6.6.6 0 1 .4 1 1V20c0 .6-.4 1-1 1A17 17 0 0 1 3 4c0-.6.4-1 1-1h3.5c.6 0 1 .4 1 1 0 1.3.2 2.5.6 3.6.1.3 0 .7-.2 1z"/></svg>
    <svg viewBox="0 0 24 24"><path d="M6 3h9l3 3v4h1a2 2 0 0 1 2 2v7a2 2 0 0 1-2 2H5a2 2 0 0 1-2-2v-7a2 2 0 0 1 2-2h1zm2 2v5h8V7h-2V5zm-1 9v2h2v-2zm4 0v2h2v-2zm4 0v2h2v-2z"/></svg>
    <svg viewBox="0 0 24 24"><path d="M3 5h18v14H3zm2 2v.5l7 5 7-5V7zm0 3v7h14v-7l-7 5z"/></svg>
  </div>
  <div class="contact-left">
    <p>713-555-0140</p>
    <p>713-555-0142</p>
    <p>dorian.taven@tavenassociateslaw.example</p>
  </div>

  <p class="website">www.tavenassociateslaw.example</p>
  <div class="website-bar"></div>

  <div class="addresses">
    <p>482 W. Birchfield Ave.<br>Suite 318<br>Houston, TX 77391</p>
    <p>56 Maple Run Center Blvd.<br>Suite 204<br>Cedar Hollow, TX 77479</p>
  </div>

  <div class="links">
    <div class="link-row">
      <svg viewBox="0 0 24 24"><path d="M6.6 10.8a15 15 0 0 0 6.6 6.6l2.2-2.2c.3-.3.7-.4 1-.2 1.1.4 2.3.6 3.6.6.6 0 1 .4 1 1V20c0 .6-.4 1-1 1A17 17 0 0 1 3 4c0-.6.4-1 1-1h3.5c.6 0 1 .4 1 1 0 1.3.2 2.5.6 3.6.1.3 0 .7-.2 1z"/></svg>
      <span>1-888-50-TAVEN</span>
    </div>
    <div class="link-row">
      <svg viewBox="0 0 24 24"><rect x="3" y="3" width="18" height="18" rx="2"/></svg>
      <span>lakeridgetrialcounsel.example</span>
    </div>
  </div>
</section>

</body>
</html>
```